Business cards and stationary design

We just completed the design of our new logo and we need to print new business cards and letterhead for our nonprofit. We are looking for a fresh new design that shows off our new logo. On letterhead, we must have a column on the right or left to include our Board of Directors (up to 45 names) (see attachment)

Industry/Entity Type

Non-Profit

Contact Information for Business Card

Standard business card with name, title, Company name, mailing address phone numbers, email address and website. Tagline on back "Opening doors to shelter"

Font styles to use
Sans Serif

Requirements
Must have
• include pertinent information above
• new logo
• fonts compatible with logo
• should use logo colors only
Nice to have
• tag lines

```html
<!DOCTYPE html>
<html lang="en">
<head>
<meta charset="UTF-8">
<title>Business Cards – Harbor Home</title>
<link href="https://fonts.googleapis.com/css2?family=Michroma&family=Libre+Baskerville&display=swap" rel="stylesheet">
<style>
  :root {
    --teal: #0a7fa0;
    --red: #e91c24;
    --ink: #444444;
    --paper: #ffffff;
    --backdrop: #d9dadb;
  }
  * { margin: 0; padding: 0; box-sizing: border-box; }
  html, body { width: 1200px; height: 1200px; overflow: hidden; }
  body {
    background: var(--backdrop);
    position: relative;
    font-family: "Libre Baskerville", Georgia, serif;
  }
  .card {
    position: absolute;
    left: 250px;
    width: 700px;
    height: 400px;
    overflow: hidden;
  }
  .card-back { top: 120px; background: var(--teal); }
  .card-front { top: 660px; background: var(--paper); }

  .tagline {
    position: absolute;
    left: 0; right: 0; top: 150px;
    text-align: center;
    color: var(--paper);
    font-family: "Michroma", "Arial", sans-serif;
    font-size: 30px;
    line-height: 1.45;
    letter-spacing: 3px;
    text-transform: uppercase;
  }
  .tagline-line {
    display: flex;
    align-items: center;
    justify-content: center;
    gap: 8px;
  }
  .tagline-rule { width: 70px; height: 1px; background: var(--paper); }

  .holder-name {
    position: absolute;
    left: 48px; top: 92px;
    font-family: "Michroma", "Arial", sans-serif;
    font-weight: 400;
    color: var(--teal);
    font-size: 22px;
    letter-spacing: 5px;
    text-transform: uppercase;
  }
  .holder-title {
    position: absolute;
    left: 50px; top: 130px;
    color: var(--ink);
    font-size: 19px;
  }
  .contact-list {
    position: absolute;
    left: 50px; top: 198px;
    list-style: none;
    color: var(--ink);
    font-size: 17px;
  }
  .contact-list li {
    display: flex;
    align-items: center;
    gap: 10px;
    height: 28px;
  }
  .contact-list li.address { align-items: flex-start; margin-top: 22px; height: auto; line-height: 26px; }
  .contact-list li.address svg { margin-top: 4px; }
  .contact-icon { flex: none; }

  .brand {
    position: absolute;
    right: 40px; top: 168px;
    display: flex;
    align-items: center;
    gap: 12px;
  }
  .brand-mark { width: 26px; height: 26px; background: var(--teal); }
  .brand-name {
    font-family: "Michroma", "Arial", sans-serif;
    color: var(--teal);
    font-size: 20px;
    letter-spacing: 2px;
    text-transform: uppercase;
  }
  .edge-band { position: absolute; left: 0; top: 0; }
</style>
</head>
<body>

<section class="card card-back" aria-label="Business card back">
  <div class="tagline">
    <div class="tagline-line"><span class="tagline-rule"></span><span>Opening doors</span><span class="tagline-rule"></span></div>
    <div class="tagline-line"><span>to shelter</span></div>
  </div>
</section>

<section class="card card-front" aria-label="Business card front">
  <svg class="edge-band" width="700" height="400" viewBox="0 0 700 400" aria-hidden="true">
    <path d="M430,400 Q540,300 700,262 L700,300 Q570,330 490,400 Z" fill="var(--red)"/>
  </svg>

  <div class="brand">
    <span class="brand-mark"></span>
    <span class="brand-name">Harbor Home</span>
  </div>

  <h1 class="holder-name">Dana Whitfield</h1>
  <p class="holder-title">Chairman</p>

  <ul class="contact-list">
    <li>
      <svg class="contact-icon" width="18" height="18" viewBox="0 0 18 18" aria-hidden="true">
        <circle cx="9" cy="9" r="9" fill="var(--teal)"/>
        <path d="M6 5 L8 5 L8.6 7.2 L7.6 8 Q8.6 10 10 10.6 L10.8 9.6 L13 10.2 L13 12 Q9 12.5 6.5 9.5 Q5.5 7.5 6 5 Z" fill="#fff"/>
      </svg>
      555.014.2870
    </li>
    <li>
      <svg class="contact-icon" width="18" height="18" viewBox="0 0 18 18" aria-hidden="true">
        <circle cx="9" cy="9" r="9" fill="var(--teal)"/>
        <circle cx="9" cy="9" r="4.5" fill="none" stroke="#fff" stroke-width="1.1"/>
        <ellipse cx="9" cy="9" rx="2" ry="4.5" fill="none" stroke="#fff" stroke-width="1"/>
        <line x1="4.5" y1="9" x2="13.5" y2="9" stroke="#fff" stroke-width="1"/>
      </svg>
      www.harborhomecoalition.org
    </li>
    <li>
      <svg class="contact-icon" width="18" height="18" viewBox="0 0 18 18" aria-hidden="true">
        <circle cx="9" cy="9" r="9" fill="var(--teal)"/>
        <rect x="5" y="6" width="8" height="6" fill="#fff"/>
        <path d="M5 6 L9 9.5 L13 6" fill="none" stroke="var(--teal)" stroke-width="0.9"/>
      </svg>
      dana@harborhomecoalition.org
    </li>
    <li class="address">
      <svg class="contact-icon" width="18" height="18" viewBox="0 0 18 18" aria-hidden="true">
        <circle cx="9" cy="9" r="9" fill="var(--teal)"/>
        <path d="M9 4 Q12.5 4 12.5 7.5 Q12.5 10 9 14 Q5.5 10 5.5 7.5 Q5.5 4 9 4 Z" fill="#fff"/>
        <circle cx="9" cy="7.5" r="1.4" fill="var(--teal)"/>
      </svg>
      <span>P.O Box 560312<br>Mesa Vista, Texas 75099</span>
    </li>
  </ul>
</section>

</body>
</html>
```